Lumora App | Pre-Launch Homepage

Dear designer,
Lumora is a soon to be launched innovative & free social platform for collaborative addictions quitting.
We require a design for our pre-launch homepage that will elevate our basic wireframes to the next level.
We would like the wireframes to serve as a guideline only, and not as a final version of the design. If you have cool ideas - we would appreciate your creativity!
* This is a pre-launch website for a mobile app, and as such the design must be consistent with the general style, design and atmosphere of the app (see screenshot in the shared Drive link).
* We liked the style and feel of the following website: http://palvexapp.com/ - Please let's use it as a reference as well.
* The existing text in the wireframes is there just to represent a place for text. Copy will be edited by us after the design is done.
Please find the wireframes attached, and all relevant design assets and app screenshots in the following Drive shared link -
https://files.norvakshare.com/open?id=7Q284KtP3mXcRf8Hj21W5vLzDne
Thanks,
Marcus
Industry/Entity Type
Social
Number of Pages Required
1 page
Look and feel
Each slider illustrates characteristics of the customer's brand and the style your logo design should communicate.

```html
<!DOCTYPE html>
<html lang="en">
<head>
<meta charset="utf-8">
<title>Lumora – Pre-Launch Homepage</title>
<link rel="stylesheet" href="https://fonts.googleapis.com/css2?family=Kaushan+Script&family=Open+Sans:wght@400;600;700&display=swap">
<style>
:root{
  --ink:#2b2b2b;
  --muted:#555;
  --peach:#fbd9b4;
  --cream:#fcebc0;
  --blush:#f7cfc9;
  --white-veil:rgba(255,255,255,.82);
  --dark-panel:rgba(40,40,40,.88);
  --green:#6fb52c;
  --green-dark:#4f8d17;
  --footer:#d9d9d9;
  --footer-bar:#1d1d1d;
  --device:#3a3a3a;
  --screen:#cfd6de;
}
*{box-sizing:border-box;margin:0;padding:0}
html,body{width:1200px;height:3404px;overflow:hidden}
body{
  position:relative;
  font-family:"Open Sans",Arial,sans-serif;color:var(--ink);
  background:linear-gradient(160deg,var(--blush) 0%,var(--cream) 30%,var(--peach) 55%,var(--cream) 75%,var(--blush) 100%);
}
.abs{position:absolute}
.script{font-family:"Kaushan Script",cursive;font-weight:400}
.center{text-align:center}

/* header */
.topbar{top:12px;right:140px;font-size:13px;color:var(--muted);display:flex;gap:26px}
.topbar span{display:flex;align-items:center;gap:6px}
.brand{top:60px;left:0;width:1200px;font-size:64px;color:#111}
.tagline{top:176px;left:0;width:1200px;font-size:22px;line-height:30px;color:#333}
.subscribe{top:288px;left:180px;width:840px;height:124px;background:var(--dark-panel);padding:18px 30px}
.subscribe p{color:#fff;font-size:20px;margin-bottom:14px}
.subscribe .field{position:absolute;left:30px;top:60px;width:530px;height:46px;background:#fff;border:1px solid #ccc;font-size:17px;color:#888;padding:12px 14px}
.subscribe .btn{position:absolute;left:580px;top:60px;width:230px;height:46px;background:linear-gradient(var(--green),var(--green-dark));color:#fff;font-weight:700;font-size:18px;display:flex;align-items:center;justify-content:center}
.hero-devices{top:470px;left:380px;width:440px;height:250px;border-radius:10px;background:linear-gradient(135deg,#e8ecef,#b8c0c8)}

/* features */
.features{top:850px;left:0;width:1200px;height:360px;background:var(--white-veil)}
.feature{position:absolute;top:60px;width:400px;text-align:center}
.feature .icon{width:90px;height:90px;border-radius:50%;margin:0 auto 22px}
.feature h3{font-size:28px;margin-bottom:12px}
.feature p{font-size:14px;line-height:20px;color:#444;width:200px;margin:0 auto}
.divider-v{position:absolute;top:80px;width:1px;height:160px;background:#ccc}

/* fun */
.phone-fun{top:1200px;left:150px;width:205px;height:440px;border-radius:34px;background:linear-gradient(#f2f2f2,#c9c9c9);border:3px solid #bbb}
.phone-fun .scr{position:absolute;left:16px;top:62px;width:167px;height:296px;background:#1a1a1a}
.fun-title{top:1210px;left:700px;font-size:44px}
.fun-copy{left:620px;width:400px;font-size:14px;line-height:21px;color:#333}

/* achieve */
.rule{top:1700px;left:150px;width:900px;height:1px;background:#bdbdbd}
.h-section{left:0;width:1200px;font-size:50px}
.achieve-lead{top:1832px;left:240px;width:720px;font-size:24px;line-height:34px;color:#333}
.achieve-sub{top:1934px;left:0;width:1200px;font-size:22px;color:#333}
.phone-center{top:2040px;left:474px;width:252px;height:390px;border-radius:26px;background:var(--device)}
.phone-center .scr{position:absolute;left:18px;top:46px;width:216px;height:296px;background:#e8e8e8;display:flex;align-items:center;justify-content:center}
.perk{width:250px;font-size:13px;line-height:18px;color:#333}
.perk-icon{width:46px;height:46px;border-radius:50%}

/* coming soon */
.soon-phone{top:2600px;left:470px;width:260px;height:340px;border-radius:24px;background:linear-gradient(135deg,#6cc4e6,#f2a54a 50%,#8a63c9)}
.arrow{top:2760px;width:40px;height:40px;border-radius:50%;border:2px solid #bbb}
.store{top:3010px;width:60px;height:60px;border-radius:12px}

/* footer */
.footer{top:3140px;left:0;width:1200px;height:240px;background:var(--footer)}
.footer h4{position:absolute;top:40px;width:1200px;text-align:center;font-size:36px}
.social{position:absolute;top:112px;left:540px;display:flex;gap:18px}
.social i{display:block;width:32px;height:32px;border-radius:50%;background:#2b2b2b}
.copy{position:absolute;top:172px;width:1200px;text-align:center;font-size:13px;color:#333}
.footbar{top:3380px;left:0;width:1200px;height:24px;background:var(--footer-bar);color:#ddd;font-size:12px;display:flex;align-items:center;justify-content:center}
</style>
</head>
<body>

<header>
  <div class="abs topbar">
    <span><svg width="16" height="12" viewBox="0 0 16 12"><rect x="0.5" y="0.5" width="15" height="11" fill="none" stroke="#555"/><path d="M1 1l7 6 7-6" fill="none" stroke="#555"/></svg>info@lumora-app.com</span>
    <span><svg width="16" height="12" viewBox="0 0 16 12"><rect x="0.5" y="0.5" width="15" height="11" fill="none" stroke="#555"/><path d="M1 1l7 6 7-6" fill="none" stroke="#555"/></svg>info@lumora-app.com</span>
  </div>
  <h1 class="abs brand center script">Lumora</h1>
  <p class="abs tagline center">Lumora is a revolutionary &amp; free social platform for collaborative<br>addictions quitting.</p>
  <form class="abs subscribe">
    <p>Subscribe below for the beta release and updates</p>
    <div class="field">Enter Your Email...</div>
    <div class="btn">LET ME KNOW!</div>
  </form>
  <div class="abs hero-devices" role="img" aria-label="App shown on desktop, tablet and phone screens"></div>
</header>

<section class="abs features">
  <div class="feature" style="left:0">
    <div class="icon" role="img" aria-label="Life ring icon" style="background:#d9432f"></div>
    <h3 class="script">Never be Alone</h3>
    <p>Forget what you know - Lumora makes it fun to quit.</p>
  </div>
  <div class="divider-v" style="left:400px"></div>
  <div class="feature" style="left:400px">
    <div class="icon" role="img" aria-label="Gold star icon" style="background:#e6b53a"></div>
    <h3 class="script">Network Power</h3>
    <p>Forget what you know - Lumora makes it fun to quit.</p>
  </div>
  <div class="divider-v" style="left:800px"></div>
  <div class="feature" style="left:800px">
    <div class="icon" role="img" aria-label="Feathered headdress icon" style="background:#6a6a6a"></div>
    <h3 class="script">Stay Motivated</h3>
    <p>Forget what you know - Lumora makes it fun to quit.</p>
  </div>
</section>

<section>
  <div class="abs phone-fun"><div class="scr" role="img" aria-label="App screen with green mascot on black"></div></div>
  <h2 class="abs fun-title script">Fun</h2>
  <p class="abs fun-copy" style="top:1300px">Forget what you know - Lumora makes it fun to quit. The battle between your good and bad themes comes to life in our gamified approach for managing your campaigns.</p>
  <p class="abs fun-copy" style="top:1448px">Lumora gives you the opportunity to take an active role in helping your network to smash your common addictions as a team. That's right, we converted the cessation process into a social game.</p>
</section>

<section>
  <div class="abs rule"></div>
  <h2 class="abs h-section center script" style="top:1740px">Achieve</h2>
  <p class="abs achieve-lead center">Lumora is built as a pyramid of relationships that makes use of the Social Cognitive Theory, to provide a powerful network of positive reinforcement.</p>
  <p class="abs achieve-sub center">The bigger you make it the stronger you get</p>

  <p class="abs perk" style="top:2100px;left:140px">Lorem ipsum is simply dummy text of the printing and typesetting industry. Lorem ipsum is simply dummy text of the printing and type setting industry.</p>
  <div class="abs perk-icon" role="img" aria-label="Trophy icon" style="top:2104px;left:400px;background:#d88a2e"></div>
  <p class="abs perk" style="top:2280px;left:140px">Lorem ipsum is simply dummy text of the printing and typesetting industry. Lorem ipsum is simply dummy text of the printing and type setting industry.</p>
  <div class="abs perk-icon" role="img" aria-label="Medal icon" style="top:2284px;left:400px;background:#e0a84a"></div>

  <div class="abs phone-center"><div class="scr">
    <svg width="120" height="120" viewBox="0 0 120 120"><circle cx="60" cy="60" r="44" fill="none" stroke="#333" stroke-width="4"/><polygon points="60,34 67,52 86,52 71,64 77,83 60,71 43,83 49,64 34,52 53,52" fill="#333"/></svg>
  </div></div>

  <div class="abs perk-icon" role="img" aria-label="Trophy icon" style="top:2104px;left:754px;background:#b0882e"></div>
  <p class="abs perk" style="top:2100px;left:812px">Lorem ipsum is simply dummy text of the printing and typesetting industry. Lorem ipsum is simply dummy text of the printing and type setting industry.</p>
  <div class="abs perk-icon" role="img" aria-label="Award icon" style="top:2284px;left:754px;background:#e38b3a"></div>
  <p class="abs perk" style="top:2280px;left:812px">Lorem ipsum is simply dummy text of the printing and typesetting industry. Lorem ipsum is simply dummy text of the printing and type setting industry.</p>
</section>

<section>
  <h2 class="abs h-section center script" style="top:2510px">Coming Soon</h2>
  <div class="abs soon-phone" role="img" aria-label="Phone with colourful app icons"></div>
  <div class="abs arrow" style="left:150px"><svg width="36" height="36" viewBox="0 0 36 36"><path d="M21 11l-7 7 7 7" fill="none" stroke="#999" stroke-width="2"/></svg></div>
  <div class="abs arrow" style="left:1014px"><svg width="36" height="36" viewBox="0 0 36 36"><path d="M15 11l7 7-7 7" fill="none" stroke="#999" stroke-width="2"/></svg></div>
  <div class="abs store" style="left:480px;background:#3fa34d"></div>
  <div class="abs store" style="left:570px;background:#2f7fd6"></div>
  <div class="abs store" style="left:660px;background:#d9342b"></div>
</section>

<footer>
  <div class="abs footer">
    <h4 class="script">Join the Revolution</h4>
    <div class="social"><i></i><i></i><i></i></div>
    <p class="copy">Copyright © 2015 Lumora Ltd.</p>
  </div>
  <nav class="abs footbar">Contact Us | FAQs | Privacy Policy</nav>
</footer>

</body>
</html>
```